IT Company Business Card Rebranding

We want to modernize our business cards massively. We want to incorporate aspects of our old business card such as the white and geometric design with the blues of another icon. Existing Logo, old business card and icon are all attached.

We are a modern IT company that provides support for new and growing technologies and want our business cards to be modern yet professional.
Updates

Note: Do not use file ICON.png in design. This is just a design we like Added Wednesday, March 9, 2016

Industry/Entity Type

Information Technology

Contact Information for Business Card

Roughly 43 : 26 or 1075 x 650 px

Font styles to use
Serif

Colors
0492cd
3276b5
33a6d7
86cfc6
cfeae6
cee9f5
ffffff

Requirements
Must have
• Modern yet professional
Nice to have
• We would like to incorporate the blues of our existing logo and of the icon provided. Really like the design of the icon.
Should not have
• Too Decorative. Just simple and professional.
• Not have the circle icon, as it is a copyrighted icon, I just like the colors and the geometric design

```html
<!DOCTYPE html>
<html lang="en">
<head>
<meta charset="utf-8">
<title>I.T. Uplift – Business Card</title>
<link href="https://fonts.googleapis.com/css2?family=Open+Sans:wght@400;600&display=swap" rel="stylesheet">
<style>
  :root {
    --stage: #2a2a2a;
    --paper: #ffffff;
    --ink: #55585c;
    --ink-soft: #6a6d72;
    --navy: #2b3f96;
    --blue: #3276b5;
    --sky: #33a6d7;
    --teal: #1e9db8;
    --deep: #2f5fb3;
  }
  * { margin: 0; padding: 0; box-sizing: border-box; }
  html, body { width: 1200px; height: 746px; overflow: hidden; }
  body {
    position: relative;
    background: var(--stage);
    font-family: "Open Sans", Arial, sans-serif;
  }
  .card {
    position: absolute;
    top: 225px;
    width: 502px;
    height: 294px;
    overflow: hidden;
    box-shadow: 0 2px 6px rgba(0,0,0,.45);
  }
  .card--front { left: 68px; background: var(--paper); }
  .card--back {
    left: 650px;
    background: linear-gradient(135deg, var(--teal) 0%, var(--deep) 45%, var(--sky) 75%, var(--blue) 100%);
  }
  .card__art { position: absolute; inset: 0; width: 100%; height: 100%; }

  .brand {
    position: absolute;
    display: flex;
    align-items: center;
    gap: 22px;
    font-weight: 400;
    letter-spacing: 6px;
    text-transform: uppercase;
  }
  .brand__dot { border-radius: 50%; flex: none; }
  .card--front .brand { left: 28px; top: 32px; font-size: 18px; color: var(--ink); }
  .card--front .brand__dot { width: 40px; height: 40px; background: var(--blue); }

  .person { position: absolute; left: 30px; top: 112px; color: var(--ink); }
  .person__name { font-size: 19px; font-weight: 400; letter-spacing: .5px; }
  .person__role { font-size: 12px; color: var(--ink-soft); margin-top: 1px; }
  .contact { list-style: none; margin-top: 10px; font-size: 12px; color: var(--ink-soft); }
  .contact li { display: flex; align-items: center; gap: 7px; height: 16px; }
  .contact svg { width: 11px; height: 11px; flex: none; }

  .card--back .brand {
    left: 0; right: 0; top: 94px;
    flex-direction: column;
    gap: 28px;
    font-size: 19px;
    color: var(--paper);
    letter-spacing: 7px;
  }
  .card--back .brand__dot { width: 66px; height: 66px; background: var(--paper); }
  .website {
    position: absolute; left: 0; right: 0; top: 247px;
    text-align: center;
    color: var(--paper);
    font-size: 11px;
    font-weight: 600;
    letter-spacing: 3px;
  }
</style>
</head>
<body>
  <section class="card card--front">
    <svg class="card__art" viewBox="0 0 502 294" aria-hidden="false">
      <defs>
        <linearGradient id="facetFront" x1="0" y1="0" x2="1" y2="1">
          <stop offset="0" stop-color="#2f5fb3"/>
          <stop offset=".5" stop-color="#1e9db8"/>
          <stop offset="1" stop-color="#3276b5"/>
        </linearGradient>
        <linearGradient id="bandNavy" x1="0" y1="0" x2="1" y2="0">
          <stop offset="0" stop-color="#3a7cc7"/>
          <stop offset="1" stop-color="#2b3f96"/>
        </linearGradient>
      </defs>
      <path role="img" aria-label="Geometric blue facet pattern"
            d="M0,222 C150,270 330,210 502,112 L502,294 L0,294 Z" fill="url(#facetFront)"/>
      <path d="M0,222 C150,270 330,210 502,112" fill="none" stroke="#ffffff" stroke-width="9"/>
      <path d="M0,208 C150,256 330,190 502,92" fill="none" stroke="url(#bandNavy)" stroke-width="18"/>
      <path d="M0,228 C150,276 330,216 502,118" fill="none" stroke="#33a6d7" stroke-width="4"/>
    </svg>

    <div class="brand"><span class="brand__dot"></span>I.T. Uplift</div>

    <div class="person">
      <h1 class="person__name">LIAM CARTER</h1>
      <p class="person__role">Technical Services</p>
      <ul class="contact">
        <li>
          <svg viewBox="0 0 12 12"><circle cx="6" cy="6" r="6" fill="#33a6d7"/><path d="M4 3.2c.4-.3.8-.2 1 .2l.5.9c.2.3.1.6-.2.8l-.3.2c.3.7.8 1.2 1.5 1.5l.2-.3c.2-.3.5-.4.8-.2l.9.5c.4.2.5.6.2 1-.5.7-1.3.8-2 .4C5.2 7.6 4.4 6.8 3.8 5.4c-.4-.8-.3-1.6.2-2.2z" fill="#fff"/></svg>
          0955 120 340
        </li>
        <li>
          <svg viewBox="0 0 12 12"><circle cx="6" cy="6" r="6" fill="#33a6d7"/><rect x="3" y="4" width="6" height="4.2" fill="#fff"/><path d="M3 4l3 2.3L9 4" fill="none" stroke="#33a6d7" stroke-width=".7"/></svg>
          liam@ituplift.com
        </li>
      </ul>
    </div>
  </section>

  <section class="card card--back" role="img" aria-label="Geometric blue facet pattern background">
    <div class="brand"><span class="brand__dot"></span>I.T. Uplift</div>
    <p class="website">www.ituplift.com</p>
  </section>
</body>
</html>
```